Cake website needs a professional WordPress design makeover!

I need a wordpress design for my company called Velvet Crumbhouse. It's a home cake business and I specialise in everything from cupcakes, celebratory cakes to couture wedding cakes. I have an existing one page wordpress website www.velvetcrumbhouse.com but it doesn't quite communicate elegance or showcase my skills so it desperately needs a complete change.

I purchased this theme
http://tilecraftery.com/demos/themes/?product=lumo
I basically want my website to look EXACTLY like this. I would obviously provide pictures of my work. I like the positioning of the pictures and texts and how each section are divided with the pictures. I also like the pop up of the welcome text on the home page. I would like that to say Welcome Velvet Crumbhouse.

One element I would like to keep from my original website are the slides on the home page. But will have a different caption with each slide. I will provide the three pictures for these slides.

The page format should be as follows:

Home
Discover Our Story
Tasteful Delights (Picture)
Discover Our Cakes - Clickable link below description going to the full cake menu with prices
The Perfect Blend (Picture)
Our Promise
Discover Your Special Day (Picture)
Wedding Cakes
Make an Order (Picture)
Get in touch

The menu on top of the page should read
Home, Our story, Our Cakes, Price List, Wedding cakes, Get in Touch

I would like to see the page of the full cake menu with the prices.
Signature colours Black, White and Pink

Target Market(s)

My main audience is targeted at women.

Industry/Entity Type

Wedding

Requirements
Must have
• Must look like the link I provided. Please use this as reference.
Nice to have
• Nice to see aspects of my logo, example the butterflies or the paisley design be subtly used around the website.

```html
<!DOCTYPE html>
<html lang="en">
<head>
<meta charset="utf-8">
<title>Velvet Crumbhouse — Our Cakes</title>
<link rel="stylesheet" href="https://fonts.googleapis.com/css2?family=Cabin:wght@400;500;600&family=Great+Vibes&family=Josefin+Sans:wght@400;600&display=swap">
<style>
  :root{
    --page:#ffffff;
    --bar:#4a2a21;
    --bar-text:#f3e6df;
    --hero-dark:#2b2522;
    --pink:#e2958c;
    --pink-soft:#f1b3a9;
    --peach:#fde3cc;
    --card:#fdf6f3;
    --ink:#3a2a25;
    --muted:#5a4842;
    --rule:#9a8a80;
    --footer:#111111;
    --footer-base:#232323;
    --footer-text:#e9e9e9;
  }
  *{box-sizing:border-box;margin:0;padding:0}
  html,body{width:1200px;height:2811px;overflow:hidden;background:var(--page)}
  body{position:relative;font-family:"Cabin",sans-serif;color:var(--ink)}

  /* ---------- hero ---------- */
  .hero{position:absolute;left:22px;top:22px;width:1156px;height:929px;overflow:hidden;
    background:radial-gradient(ellipse 52% 46% at 47% 42%,#f4f2ef 0%,#e3e0dc 45%,#b9b4ae 62%,#4a3f39 78%,var(--hero-dark) 100%)}
  .hero-photo{position:absolute;inset:0}
  .site-bar{position:absolute;left:0;top:0;width:100%;height:69px;background:rgba(74,42,33,.92);
    display:flex;align-items:center}
  .brand{position:absolute;left:20px;top:20px;display:flex;align-items:center;gap:12px;
    font-family:"Cabin",sans-serif;font-size:24px;color:var(--bar-text)}
  .brand-dot{width:14px;height:14px;border-radius:50%;background:var(--pink-soft)}
  .main-nav a{position:absolute;top:22px;font-size:16px;color:var(--bar-text);text-decoration:none;white-space:nowrap}
  .main-nav a.current{border-bottom:2px solid var(--bar-text);padding-bottom:6px}
  .nav-caret{display:inline-block;width:7px;height:7px;border-right:1.5px solid var(--bar-text);border-bottom:1.5px solid var(--bar-text);transform:rotate(45deg);margin-left:7px;position:relative;top:-3px}
  .bar-icon{position:absolute;top:28px;width:12px;height:12px;border-radius:50%;background:var(--bar-text)}
  .cart-badge{position:absolute;left:1128px;top:38px;width:12px;height:12px;border-radius:50%;background:var(--pink)}

  .hero-script{position:absolute;left:0;width:100%;top:388px;text-align:center;
    font-family:"Great Vibes",cursive;font-size:82px;color:var(--pink);line-height:1}
  .hero-title{position:absolute;left:0;width:100%;top:462px;text-align:center;
    font-family:"Josefin Sans",sans-serif;font-weight:600;font-size:50px;letter-spacing:5px;color:#fff}
  .hero-rule{position:absolute;left:330px;top:500px}
  .hero-mark{position:absolute;left:0;width:100%;top:655px;display:flex;justify-content:center;align-items:center;gap:14px;
    font-family:"Cabin",sans-serif;font-size:34px;color:var(--pink)}
  .hero-mark span.square{width:22px;height:22px;background:var(--pink)}
  .slide-dots{position:absolute;left:1092px;top:468px;display:flex;flex-direction:column;gap:16px}
  .slide-dots i{display:block;width:13px;height:13px;border-radius:50%;border:2px solid #fff}
  .slide-dots i.on{background:#fff}
  .hero-notch{position:absolute;left:516px;bottom:-1px}

  /* ---------- cakes ---------- */
  .cakes{position:absolute;left:22px;top:1005px;width:1156px;height:1157px;background:var(--peach)}
  .edge{position:absolute;left:0;width:100%}
  .edge-top{top:-12px}
  .tabs{position:absolute;left:47px;top:52px;display:flex;gap:7px}
  .tab{height:52px;display:flex;align-items:center;justify-content:center;font-size:27px}
  .tab-prices{width:175px;background:var(--bar);color:#fff}
  .tab-desc{width:177px;background:var(--pink);color:#fff;border:2px solid var(--bar)}
  .pager{position:absolute;left:1003px;top:65px;display:flex;gap:4px}
  .pager span{width:48px;height:40px;background:var(--pink);display:flex;align-items:center;justify-content:center}

  .cake-grid{position:absolute;left:47px;top:119px;display:grid;grid-template-columns:repeat(4,253px);
    grid-auto-rows:450px;column-gap:16px;row-gap:50px}
  .cake-card{position:relative;background:var(--card)}
  .cake-photo{position:absolute;left:15px;top:15px;width:223px;height:314px}
  .cake-name{position:absolute;left:15px;top:336px;font-size:20px;color:var(--pink);text-transform:uppercase;white-space:nowrap}
  .cake-note{position:absolute;left:15px;top:370px;font-size:15px;color:var(--ink)}
  .cake-actions{position:absolute;left:15px;top:412px;display:flex;gap:12px;align-items:center}
  .cake-price{position:absolute;right:15px;top:396px;width:82px;height:40px;background:var(--pink);color:#fff;
    display:flex;align-items:center;justify-content:center;font-size:27px}
  .section-rule{position:absolute;left:47px;top:1108px}

  /* ---------- footer ---------- */
  .contact{position:absolute;left:22px;top:2162px;width:1156px;height:530px;background:var(--footer);color:var(--footer-text);text-align:center}
  .contact .edge-top{top:-14px}
  .contact-heading{position:absolute;left:0;width:100%;top:72px;font-size:21px;letter-spacing:3px}
  .contact-star{position:absolute;left:0;width:100%;top:118px;color:var(--pink);font-size:20px}
  .contact-lines{position:absolute;left:0;width:100%;top:164px;font-size:16px;letter-spacing:1.5px;line-height:27px}
  .follow{position:absolute;left:295px;width:200px;top:322px}
  .newsletter{position:absolute;left:640px;width:240px;top:322px}
  .label{font-size:15px;letter-spacing:2px}
  .social{display:flex;justify-content:center;gap:34px;margin-top:34px}
  .social i{width:16px;height:16px;border-radius:50%;background:var(--footer-text);display:block}
  .signup{margin-top:22px;display:flex;width:238px;height:37px;background:#fff;align-items:center;justify-content:space-between;padding:0 12px}
  .signup span{font-size:13px;color:#999}
  .to-top{position:absolute;left:530px;top:478px}
  .base{position:absolute;left:22px;top:2692px;width:1156px;height:97px;background:var(--footer-base);color:var(--footer-text);
    display:flex;align-items:center;justify-content:center;font-size:13px;letter-spacing:2px}
</style>
</head>
<body>

<header class="hero">
  <div class="hero-photo" role="img" aria-label="Photograph of a chocolate dessert with sauce and mint in a white bowl on a dark woven mat"></div>
  <div class="site-bar">
    <div class="brand"><span class="brand-dot"></span>Velvet Crumbhouse</div>
    <nav class="main-nav">
      <a class="current" style="left:367px">Home</a>
      <a style="left:458px">Our Story</a>
      <a style="left:548px">Our Cakes<span class="nav-caret"></span></a>
      <a style="left:660px">Price List</a>
      <a style="left:776px">Wedding Cakes</a>
      <a style="left:900px">Get in Touch</a>
    </nav>
    <i class="bar-icon" style="left:1028px"></i>
    <i class="bar-icon" style="left:1068px"></i>
    <svg style="position:absolute;left:1106px;top:26px" width="22" height="20" viewBox="0 0 22 20"><path d="M1 2h4l3 11h10l3-8H7" fill="none" stroke="#f3e6df" stroke-width="2"/><circle cx="9" cy="17" r="1.8" fill="#f3e6df"/><circle cx="17" cy="17" r="1.8" fill="#f3e6df"/></svg>
    <span class="cart-badge"></span>
  </div>

  <div class="hero-script">Our Cakes</div>
  <h1 class="hero-title">VELVET CRUMBHOUSE</h1>
  <svg class="hero-rule" width="496" height="40" viewBox="0 0 496 40">
    <line x1="0" y1="24" x2="496" y2="24" stroke="#fff" stroke-width="2"/>
    <circle cx="2" cy="24" r="3" fill="#fff"/><circle cx="494" cy="24" r="3" fill="#fff"/>
    <text x="248" y="40" text-anchor="middle" fill="#e2958c" font-size="20" font-family="Cabin,sans-serif">*</text>
  </svg>
  <div class="hero-mark"><span class="square"></span>Velvet Crumbhouse</div>

  <div class="slide-dots"><i class="on"></i><i></i><i></i><i></i></div>
  <svg class="hero-notch" width="124" height="40" viewBox="0 0 124 40">
    <path d="M0 40 C30 40 34 6 62 6 C90 6 94 40 124 40Z" fill="#fff"/>
    <path d="M51 18l11 10 11-10" fill="none" stroke="#4a2a21" stroke-width="2.5"/>
  </svg>
</header>

<main class="cakes">
  <svg class="edge edge-top" width="1156" height="13" viewBox="0 0 1156 13" preserveAspectRatio="none">
    <defs><pattern id="teeth-peach" width="14" height="13" patternUnits="userSpaceOnUse"><path d="M0 13 L7 1 L14 13Z" fill="#fde3cc"/></pattern></defs>
    <rect width="1156" height="13" fill="url(#teeth-peach)"/>
  </svg>

  <div class="tabs">
    <div class="tab tab-prices">Prices</div>
    <div class="tab tab-desc">Description</div>
  </div>
  <div class="pager">
    <span><svg width="14" height="20" viewBox="0 0 14 20"><path d="M11 2L3 10l8 8" fill="none" stroke="#fff" stroke-width="3"/></svg></span>
    <span><svg width="14" height="20" viewBox="0 0 14 20"><path d="M3 2l8 8-8 8" fill="none" stroke="#fff" stroke-width="3"/></svg></span>
  </div>

  <div class="cake-grid">
    <article class="cake-card">
      <div class="cake-photo" role="img" aria-label="Photograph of a white ruffled three tier wedding cake" style="background:linear-gradient(180deg,#ece6df,#d8cfc4 60%,#bfb2a3)"></div>
      <h2 class="cake-name">Wedding Cakes</h2><p class="cake-note">Simple iced 3 tier</p>
      <div class="cake-actions"><svg width="16" height="14" viewBox="0 0 16 14"><path d="M8 14L1.5 7.5A3.8 3.8 0 0 1 8 2.5a3.8 3.8 0 0 1 6.5 5Z" fill="#3a2a25"/></svg><svg width="16" height="14" viewBox="0 0 16 14"><path d="M0 1h3l2 8h8l2-6H4" fill="none" stroke="#3a2a25" stroke-width="1.8"/><circle cx="6" cy="12.5" r="1.3" fill="#3a2a25"/><circle cx="12" cy="12.5" r="1.3" fill="#3a2a25"/></svg></div>
      <div class="cake-price">£250</div>
    </article>
    <article class="cake-card">
      <div class="cake-photo" role="img" aria-label="Photograph of a pink lace-patterned occasion cake on a glass stand" style="background:linear-gradient(180deg,#d9c6c2,#d98c86 45%,#c9b8b6)"></div>
      <h2 class="cake-name">Occasion Cakes</h2>
      <div class="cake-actions"><svg width="16" height="14" viewBox="0 0 16 14"><path d="M8 14L1.5 7.5A3.8 3.8 0 0 1 8 2.5a3.8 3.8 0 0 1 6.5 5Z" fill="#3a2a25"/></svg><svg width="16" height="14" viewBox="0 0 16 14"><path d="M0 1h3l2 8h8l2-6H4" fill="none" stroke="#3a2a25" stroke-width="1.8"/><circle cx="6" cy="12.5" r="1.3" fill="#3a2a25"/><circle cx="12" cy="12.5" r="1.3" fill="#3a2a25"/></svg></div>
      <div class="cake-price">£35</div>
    </article>
    <article class="cake-card">
      <div class="cake-photo" role="img" aria-label="Photograph of a slice of rainbow layer cake on a plate" style="background:linear-gradient(180deg,#d8d4d0 0%,#e65a4e 30%,#f2b63c 45%,#6fbf5a 60%,#4a78c8 75%,#e8e4e0 100%)"></div>
      <h2 class="cake-name">Classic Layer Cakes</h2>
      <div class="cake-actions"><svg width="16" height="14" viewBox="0 0 16 14"><path d="M8 14L1.5 7.5A3.8 3.8 0 0 1 8 2.5a3.8 3.8 0 0 1 6.5 5Z" fill="#3a2a25"/></svg><svg width="16" height="14" viewBox="0 0 16 14"><path d="M0 1h3l2 8h8l2-6H4" fill="none" stroke="#3a2a25" stroke-width="1.8"/><circle cx="6" cy="12.5" r="1.3" fill="#3a2a25"/><circle cx="12" cy="12.5" r="1.3" fill="#3a2a25"/></svg></div>
      <div class="cake-price">£25</div>
    </article>
    <article class="cake-card">
      <div class="cake-photo" role="img" aria-label="Photograph of a chocolate sponge square with a raspberry on red sauce" style="background:linear-gradient(180deg,#8a7a72,#4a2a22 50%,#8e1a1e 85%,#d9cfc9)"></div>
      <h2 class="cake-name">Whoopie Pies</h2><p class="cake-note">Minimum order of 12</p>
      <div class="cake-actions"><svg width="16" height="14" viewBox="0 0 16 14"><path d="M8 14L1.5 7.5A3.8 3.8 0 0 1 8 2.5a3.8 3.8 0 0 1 6.5 5Z" fill="#3a2a25"/></svg><svg width="16" height="14" viewBox="0 0 16 14"><path d="M0 1h3l2 8h8l2-6H4" fill="none" stroke="#3a2a25" stroke-width="1.8"/><circle cx="6" cy="12.5" r="1.3" fill="#3a2a25"/><circle cx="12" cy="12.5" r="1.3" fill="#3a2a25"/></svg></div>
      <div class="cake-price">£2.50</div>
    </article>

    <article class="cake-card">
      <div class="cake-photo" role="img" aria-label="Photograph of a chocolate cupcake with swirled frosting" style="background:linear-gradient(180deg,#a3714f,#c89a78 40%,#3a2a24 75%,#2a201c)"></div>
      <h2 class="cake-name">Cupcakes</h2><p class="cake-note">Minimum order of 12</p>
      <div class="cake-actions"><svg width="16" height="14" viewBox="0 0 16 14"><path d="M8 14L1.5 7.5A3.8 3.8 0 0 1 8 2.5a3.8 3.8 0 0 1 6.5 5Z" fill="#3a2a25"/></svg><svg width="16" height="14" viewBox="0 0 16 14"><path d="M0 1h3l2 8h8l2-6H4" fill="none" stroke="#3a2a25" stroke-width="1.8"/><circle cx="6" cy="12.5" r="1.3" fill="#3a2a25"/><circle cx="12" cy="12.5" r="1.3" fill="#3a2a25"/></svg></div>
      <div class="cake-price">£2.50</div>
    </article>
    <article class="cake-card">
      <div class="cake-photo" role="img" aria-label="Photograph of mini cupcakes decorated as sunflowers" style="background:linear-gradient(180deg,#6a5a3a,#f0dc8a 35%,#e8c658 60%,#e46a8a 90%)"></div>
      <h2 class="cake-name">Mini Cupcakes</h2><p class="cake-note">Minimum order of 12</p>
      <div class="cake-actions"><svg width="16" height="14" viewBox="0 0 16 14"><path d="M8 14L1.5 7.5A3.8 3.8 0 0 1 8 2.5a3.8 3.8 0 0 1 6.5 5Z" fill="#3a2a25"/></svg><svg width="16" height="14" viewBox="0 0 16 14"><path d="M0 1h3l2 8h8l2-6H4" fill="none" stroke="#3a2a25" stroke-width="1.8"/><circle cx="6" cy="12.5" r="1.3" fill="#3a2a25"/><circle cx="12" cy="12.5" r="1.3" fill="#3a2a25"/></svg></div>
      <div class="cake-price">£2.00</div>
    </article>
    <article class="cake-card">
      <div class="cake-photo" role="img" aria-label="Photograph of chocolate truffles and pink cake pops" style="background:linear-gradient(180deg,#e3a0b0,#4a2e26 45%,#2c1c18 70%,#e8e2dc)"></div>
      <h2 class="cake-name">Cake Pops &amp; Truffles</h2><p class="cake-note">Minimum order of 12</p>
      <div class="cake-actions"><svg width="16" height="14" viewBox="0 0 16 14"><path d="M8 14L1.5 7.5A3.8 3.8 0 0 1 8 2.5a3.8 3.8 0 0 1 6.5 5Z" fill="#3a2a25"/></svg><svg width="16" height="14" viewBox="0 0 16 14"><path d="M0 1h3l2 8h8l2-6H4" fill="none" stroke="#3a2a25" stroke-width="1.8"/><circle cx="6" cy="12.5" r="1.3" fill="#3a2a25"/><circle cx="12" cy="12.5" r="1.3" fill="#3a2a25"/></svg></div>
      <div class="cake-price">£2.00</div>
    </article>
    <article class="cake-card">
      <div class="cake-photo" role="img" aria-label="Photograph of a chocolate loaf cake slice with a raspberry on red sauce" style="background:linear-gradient(180deg,#8a7a72,#4a2a22 50%,#8e1a1e 85%,#d9cfc9)"></div>
      <h2 class="cake-name">Loaf Cakes</h2>
      <div class="cake-actions"><svg width="16" height="14" viewBox="0 0 16 14"><path d="M8 14L1.5 7.5A3.8 3.8 0 0 1 8 2.5a3.8 3.8 0 0 1 6.5 5Z" fill="#3a2a25"/></svg><svg width="16" height="14" viewBox="0 0 16 14"><path d="M0 1h3l2 8h8l2-6H4" fill="none" stroke="#3a2a25" stroke-width="1.8"/><circle cx="6" cy="12.5" r="1.3" fill="#3a2a25"/><circle cx="12" cy="12.5" r="1.3" fill="#3a2a25"/></svg></div>
      <div class="cake-price">£15</div>
    </article>
  </div>

  <svg class="section-rule" width="1062" height="20" viewBox="0 0 1062 20">
    <line x1="4" y1="10" x2="518" y2="10" stroke="#9a8a80" stroke-width="2"/>
    <line x1="544" y1="10" x2="1058" y2="10" stroke="#9a8a80" stroke-width="2"/>
    <path d="M0 4v12l8-6Z M1062 4v12l-8-6Z" fill="#9a8a80"/>
    <text x="531" y="17" text-anchor="middle" fill="#9a8a80" font-size="20" font-family="Cabin,sans-serif">*</text>
  </svg>
</main>

<footer class="contact">
  <svg class="edge edge-top" width="1156" height="15" viewBox="0 0 1156 15" preserveAspectRatio="none">
    <defs><pattern id="teeth-dark" width="14" height="15" patternUnits="userSpaceOnUse"><path d="M0 15 L7 1 L14 15Z" fill="#111111"/></pattern></defs>
    <rect width="1156" height="15" fill="url(#teeth-dark)"/>
  </svg>
  <h2 class="contact-heading">GET IN TOUCH</h2>
  <div class="contact-star">*</div>
  <div class="contact-lines">VELVET CRUMBHOUSE<br>London,United Kingdom<br>Tel:+44 7000 118245</div>

  <div class="follow">
    <div class="label">FOLLOW ALONG</div>
    <div class="social"><i></i><i></i><i></i><i></i></div>
  </div>
  <div class="newsletter">
    <div class="label">NEWSLETTER</div>
    <div class="signup"><span>Your email address</span>
      <svg width="14" height="11" viewBox="0 0 14 11"><rect width="14" height="11" fill="#333"/><path d="M0 0l7 6 7-6" fill="none" stroke="#fff" stroke-width="1.4"/></svg></div>
  </div>

  <svg class="to-top" width="96" height="52" viewBox="0 0 96 52">
    <path d="M0 52 C24 52 26 6 48 6 C70 6 72 52 96 52Z" fill="#232323"/>
    <path d="M42 30l6-6 6 6 M42 36l6-6 6 6" fill="none" stroke="#e9e9e9" stroke-width="2"/>
  </svg>
</footer>
<div class="base">© VELVET CRUMBHOUSE</div>

</body>
</html>
```